Website for Torvel Capital - investment banking firm

We have a corporate identity (thanks to Ranjita/41238) and want to extend that into a website design.  See the attached zipped files.
We have software folks in-house to do the coding.
See the attached Project Brief & Notes for more details.  Don't worry about the actual text - lorem ipsum will be fine.
The server will be Apache.
Thank you!
Desmond

```html
<!DOCTYPE html>
<html lang="en">
<head>
<meta charset="utf-8">
<title>Torvel Capital</title>
<link href="https://fonts.googleapis.com/css2?family=Cinzel:wght@400;700&family=Lato:ital,wght@0,400;0,700;1,400&family=Ubuntu:wght@400&display=swap" rel="stylesheet">
<style>
:root{
  --navy:#0b3a7a;
  --navy-deep:#02336f;
  --brand:#1e4e9a;
  --ink:#2b2b2b;
  --grey:#6e6e6e;
  --line:#cfcfcf;
  --sky:#4a9ad6;
  --white:#ffffff;
}
*{margin:0;padding:0;box-sizing:border-box}
html,body{width:1200px;height:1148px;overflow:hidden}
body{position:relative;background:var(--white);font-family:"Lato",sans-serif;color:var(--ink)}
.abs{position:absolute}

/* header */
.site-header{position:absolute;left:0;top:0;width:1200px;height:95px;background:var(--white)}
.follow{left:131px;top:38px;display:flex;align-items:center;gap:8px;font-family:"Cinzel",serif;font-weight:700;font-size:21px;color:var(--brand)}
.social{display:flex;gap:8px;margin-left:4px}
.social span{width:26px;height:26px;border-radius:50%;background:#777}
.brand{left:431px;top:16px;display:flex;align-items:center;gap:14px}
.brand-mark{width:54px;height:54px;background:var(--brand)}
.brand-name{font-family:"Cinzel",serif;font-weight:700;font-size:36px;color:var(--brand);letter-spacing:.5px;padding-left:14px;border-left:2px solid #666;line-height:64px}
.call{left:847px;top:29px;display:flex;align-items:center;gap:12px}
.call-icon{width:40px;height:40px;border:3px solid #444;border-radius:50%;display:flex;align-items:center;justify-content:center}
.call-text small{display:block;font-family:"Cinzel",serif;font-weight:700;font-size:16px;color:var(--brand);line-height:16px}
.call-text strong{display:block;font-family:"Cinzel",serif;font-weight:400;font-size:27px;color:#333;line-height:30px}

/* navigation */
.main-nav{position:absolute;left:0;top:95px;width:1200px;height:41px;background:linear-gradient(#2f62ad,#123f86)}
.main-nav ul{position:absolute;left:131px;display:flex;list-style:none;height:41px}
.main-nav li{height:41px;display:flex;align-items:center;justify-content:center;font-family:"Cinzel",serif;font-size:16px;color:var(--white);border-right:1px solid #0a2f66;letter-spacing:.5px}
.main-nav li.active{background:linear-gradient(#6fa8dc,#3a7cc2)}

/* backdrop and hero */
.backdrop{position:absolute;left:0;top:136px;width:1200px;height:792px;background:linear-gradient(90deg,#dfe3e8,#f4f5f7 30%,#f4f5f7 70%,#d8dde3)}
.hero{position:absolute;left:131px;top:136px;width:938px;height:516px;background:linear-gradient(160deg,#b9b4e8 0%,#6d8fc9 35%,#335d93 65%,#1c2a44 100%)}
.hero-caption{position:absolute;left:131px;top:216px;width:535px;height:148px;background:rgba(240,242,250,.88);clip-path:polygon(0 0,100% 0,94% 100%,0 100%)}
.hero-caption h1{position:absolute;left:17px;top:8px;font-family:"Cinzel",serif;font-weight:700;font-size:40px;color:var(--brand);white-space:nowrap}
.hero-caption p{position:absolute;left:17px;top:56px;width:470px;font-family:"Ubuntu",sans-serif;font-size:20px;line-height:27px;color:#333}

/* content panel */
.panel{position:absolute;left:131px;top:652px;width:938px;height:337px;background:var(--white);box-shadow:0 2px 6px rgba(0,0,0,.2)}
.divider{position:absolute;top:700px;width:1px;height:220px;background:linear-gradient(transparent,#ddd 20%,#ddd 80%,transparent)}
.col-title{position:absolute;font-family:"Cinzel",serif;font-weight:700;font-size:24px;color:#333;white-space:nowrap}
.col-title em{font-style:normal;color:var(--brand)}
.title-rule{position:absolute;height:1px;background:#bbb}
.title-rule::after{content:"";position:absolute;left:10px;top:0;width:9px;height:9px;border-right:1px solid #bbb;border-bottom:1px solid #bbb;background:var(--white);transform:rotate(45deg) translate(-4px,-4px)}
.read-more{position:absolute;top:930px;font-size:13px;font-weight:700;color:#333}

.about-photo{position:absolute;left:147px;top:733px;width:268px;height:103px;background:linear-gradient(90deg,#c9d3dc,#e8e4dc 40%,#3a3f4a 70%,#d6d6d6)}
.about-text{position:absolute;left:147px;top:845px;width:270px;font-size:13px;line-height:19.5px;letter-spacing:.6px;color:#333}

.service{position:absolute;left:473px;width:265px;display:flex;align-items:center;gap:10px;font-size:15px;font-weight:700;color:#444;line-height:18px}
.service svg{flex:none}
.service .sep{width:1px;height:26px;background:#ccc}
.service-rule{position:absolute;left:473px;width:265px;height:3px;background:linear-gradient(#e3e3e3,#fafafa)}

.quote{position:absolute;left:790px;top:732px;width:263px;height:129px;background:#e4e4e6;border-radius:8px}
.quote::after{content:"";position:absolute;right:40px;bottom:-18px;border-top:18px solid #e4e4e6;border-left:28px solid transparent}
.quote-mark{position:absolute;left:10px;top:12px}
.quote p{position:absolute;left:12px;top:14px;width:248px;font-style:italic;font-size:13px;line-height:22.5px;color:#333;text-indent:31px}
.avatar{position:absolute;left:802px;top:849px;width:66px;height:66px;border:3px solid var(--white);border-radius:5px;background:linear-gradient(#8a6a55,#3b4a66);box-shadow:0 1px 4px rgba(0,0,0,.35)}
.client-name{position:absolute;left:880px;top:885px;font-size:13px;color:#222}

/* footer */
.site-footer{position:absolute;left:0;top:928px;width:1200px;height:220px;background:var(--navy-deep);border-top:3px solid #7a8ea8}
.footer-nav{position:absolute;left:137px;top:1016px;display:flex;font-size:13.5px;color:var(--white)}
.footer-nav span+span::before{content:"|";margin:0 10px}
.newsletter{position:absolute;left:134px;top:1053px;display:flex;align-items:center}
.nl-icon{width:34px;height:34px;border-radius:50%;border:2px solid var(--white);background:var(--navy-deep);display:flex;align-items:center;justify-content:center;position:relative;z-index:1}
.nl-field{width:150px;height:33px;margin-left:-8px;background:var(--white);border-radius:0 4px 4px 0;font-size:11px;color:#999;padding:10px 0 0 20px}
.nl-button{margin-left:4px;height:33px;padding:0 8px;background:var(--sky);color:var(--white);font-size:14px;line-height:33px;border-radius:3px}
.copyright{position:absolute;left:134px;top:1106px;font-size:12.5px;color:var(--white)}
.contact-list{position:absolute;left:795px;top:1012px;color:var(--white);font-size:13.5px}
.contact-row{position:relative;padding-left:26px}
.contact-row svg{position:absolute;left:2px;top:2px}
.addr{line-height:16px}
.phone{margin-top:12px;font-weight:700;letter-spacing:.8px}
.email{margin-top:13px;letter-spacing:.6px}
</style>
</head>
<body>

<header class="site-header">
  <div class="follow abs">Follow Us :
    <div class="social"><span></span><span></span><span></span></div>
  </div>
  <div class="brand abs">
    <div class="brand-mark"></div>
    <div class="brand-name">TORVEL CAPITAL</div>
  </div>
  <div class="call abs">
    <div class="call-icon">
      <svg width="20" height="20" viewBox="0 0 20 20"><path d="M5 2c-2 1-3 3-2 6 2 5 5 8 9 10 3 1 5 0 6-2l-3-3-2 2c-3-1-5-4-6-6l2-2z" fill="#444"/></svg>
    </div>
    <div class="call-text"><small>Have a Question ?</small><strong>214-555-0187</strong></div>
  </div>
</header>

<nav class="main-nav">
  <ul>
    <li class="active" style="width:99px">HOME</li>
    <li style="width:93px">ABOUT</li>
    <li style="width:108px">SERVICES</li>
    <li style="width:234px">CURRENT ENGAGEMENTS</li>
    <li style="width:258px">COMPLETED TRANSACTIONS</li>
    <li style="width:146px;border-right:none">CONTACT US</li>
  </ul>
</nav>

<div class="backdrop" role="img" aria-label="Bright office interior with tall windows"></div>
<div class="hero" role="img" aria-label="Two businessmen shaking hands in front of a glass office tower"></div>
<div class="hero-caption">
  <h1>TORVEL CAPITAL LLC IS</h1>
  <p>Dallas-based private investment banking advisory firm that acts as an intermediary on behalf of buyers &amp; sellers of private companies.</p>
</div>

<div class="site-footer"></div>
<section class="panel"></section>
<div class="divider" style="left:434px"></div>
<div class="divider" style="left:753px"></div>

<!-- About column -->
<h2 class="col-title" style="left:152px;top:683px">About <em>Torvel Capital</em></h2>
<div class="title-rule" style="left:152px;top:718px;width:266px"></div>
<div class="about-photo" role="img" aria-label="Colleagues talking around a table"></div>
<p class="about-text">Torvel Capital's history in mergers and acquisitions traces back to 1998. We pride our selves in successfully matching buyers with sellers and enabling shareholders of all .</p>
<a class="read-more" style="left:340px">Read More »</a>

<!-- Services column -->
<h2 class="col-title" style="left:472px;top:683px">What <em>We Do</em></h2>
<div class="title-rule" style="left:473px;top:718px;width:265px"></div>
<div class="service" style="top:740px">
  <svg width="40" height="30" viewBox="0 0 40 30"><path d="M2 10l10-6 8 4 8-4 10 6-8 10-6 4-6-3-6-3z" fill="none" stroke="#777" stroke-width="2.5"/></svg>
  <span class="sep"></span><span>Buy-Side Acquisitions</span>
</div>
<div class="service-rule" style="top:779px"></div>
<div class="service" style="top:799px">
  <svg width="34" height="34" viewBox="0 0 34 34"><g fill="#777"><rect x="2" y="22" width="5" height="10"/><rect x="10" y="17" width="5" height="15"/><rect x="18" y="12" width="5" height="20"/><rect x="26" y="7" width="5" height="25"/></g><text x="12" y="11" font-size="12" font-weight="700" fill="#777" font-family="Lato,sans-serif">$</text></svg>
  <span class="sep"></span><span>Recapitalizations &amp;<br>Growth Capital Partnerships</span>
</div>
<div class="service-rule" style="top:848px"></div>
<div class="service" style="top:872px">
  <svg width="34" height="34" viewBox="0 0 34 34"><text x="10" y="14" font-size="15" font-weight="700" fill="#777" font-family="Lato,sans-serif">$</text><path d="M2 22h12l6 3h10v5H10l-8-3z" fill="#777"/></svg>
  <span class="sep"></span><span>Sell-Side Transactions</span>
</div>
<a class="read-more" style="left:660px">Read More »</a>

<!-- Testimonials column -->
<h2 class="col-title" style="left:789px;top:683px">Client <em>Testimonials</em></h2>
<div class="title-rule" style="left:790px;top:718px;width:264px"></div>
<div class="quote">
  <svg class="quote-mark" width="24" height="18" viewBox="0 0 24 18"><path d="M0 6a6 6 0 016-6h4v9H5v9H0zM13 6a6 6 0 016-6h5v9h-5v9h-6z" fill="#bbb"/></svg>
  <p>Duis autem vel eum iriureol hder in a vultat velit esse moles conqat vela ilu adipsin feugiat.Duis autem vel eum ure hendrern vultat velit esse autm vel eum iriure dol</p>
</div>
<div class="avatar" role="img" aria-label="Client portrait"></div>
<div class="client-name">Mr. Dolore Eu Feugiat</div>
<a class="read-more" style="left:976px">Read More »</a>

<!-- Footer content -->
<nav class="footer-nav">
  <span>Home</span><span>About</span><span>Services</span><span>Current Engagements</span><span>Completed Transactions</span><span>Contact Us</span>
</nav>
<div class="newsletter">
  <div class="nl-icon"><svg width="16" height="12" viewBox="0 0 16 12"><rect x="0.5" y="0.5" width="15" height="11" fill="#fff"/><path d="M1 1l7 6 7-6" fill="none" stroke="#02336f" stroke-width="1.5"/></svg></div>
  <div class="nl-field">Sign Up for Newsletter</div>
  <div class="nl-button">SUBSCRIBE</div>
</div>
<p class="copyright">© Copyright 2014 Torvel Capital. | All Rights Reserved</p>

<address class="contact-list" style="font-style:normal">
  <div class="contact-row addr">
    <svg width="12" height="18" viewBox="0 0 12 18"><path d="M6 0a6 6 0 016 6c0 4-6 12-6 12S0 10 0 6a6 6 0 016-6z" fill="#fff"/><circle cx="6" cy="6" r="2.2" fill="#02336f"/></svg>
    Hong Kong: Room 1804 Harbourline Tower<br>12 - 18 Lockhart Road East<br>Wanchai, Hong Kong
  </div>
  <div class="contact-row phone">
    <svg width="16" height="14" viewBox="0 0 16 14"><path d="M3 1C1 2 0 4 2 7c2 3 5 6 8 6 2 0 3-1 4-2l-3-2-2 1C7 9 5 7 4 5l1-2z" fill="#fff"/></svg>
    214-555-0187
  </div>
  <div class="contact-row email">
    <svg width="16" height="12" viewBox="0 0 16 12"><rect width="16" height="11" fill="#fff"/><path d="M0 0l8 6 8-6" fill="none" stroke="#02336f" stroke-width="1.4"/></svg>
    info@torvelcapital.com
  </div>
</address>

</body>
</html>
```